New Record Label needs a Web design

We are Iron Heron: a London based, new & independent music production company aimed at the 25-40 age group. The musical style is Soul/Classic Brelvane.
We have at the moment just one signed artist, but will expand in the future.
We dont' have any webpage yet and are looking for an innovative web design for our webpage www.iron-heron-example.com
I have uploaded our company logo.

Initially the whole website will only have 3 tabs: Home page/Artists/Contact

The design should be classic and high-end, but can be a bit crazy too.

```html
<!DOCTYPE html>
<html lang="en">
<head>
<meta charset="utf-8">
<title>Iron Heron — Home page</title>
<link rel="stylesheet" href="https://fonts.googleapis.com/css2?family=Arimo:wght@400;500;700&family=Inter:wght@300;400;500&display=swap">
<style>
  :root {
    --red: #ee3a3a;
    --red-soft: #f28a8a;
    --ink: #444444;
    --ink-soft: #7a7a7a;
    --bar: #4d4b4c;
    --paper: #ffffff;
    --band: #f4f4f4;
    --line: #555555;
    --tweet-blue: #4aa3e6;
  }
  * { box-sizing: border-box; margin: 0; padding: 0; }
  html, body { width: 1013px; height: 1200px; overflow: hidden; background: var(--paper); }
  body { position: relative; font-family: "Arimo", Arial, sans-serif; color: var(--ink); }
  .abs { position: absolute; }

  .top-bar { left: 0; top: 0; width: 1013px; height: 8px; background: var(--bar); }
  .nav-marker { left: 577px; top: 8px; width: 122px; height: 19px; background: var(--red); }

  .brand { left: 101px; top: 66px; display: flex; align-items: center; gap: 10px; }
  .brand-dot { width: 22px; height: 22px; border-radius: 50%; background: var(--red); }
  .brand-name { font-family: "Inter", sans-serif; font-weight: 400; font-size: 26px; color: var(--red); letter-spacing: .5px; }

  .main-nav { top: 84px; left: 0; width: 1013px; height: 20px; font-family: "Inter", sans-serif; font-size: 16px; }
  .main-nav a { position: absolute; text-decoration: none; color: var(--ink); }
  .main-nav a.current { color: var(--red); }

  .hero-photo { left: 0; top: 160px; width: 1013px; height: 437px;
    background: radial-gradient(ellipse at 50% 45%, #6a6a6a 0%, #3a3a3a 22%, #9a9a9a 42%, #e6e6e6 65%, #f2f2f2 100%); }
  .hero-name { left: 108px; top: 482px; font-family: "Inter", sans-serif; font-weight: 300; font-size: 34px; color: #333; }
  .more-details { left: 746px; top: 439px; width: 142px; height: 24px; border-radius: 12px; background: #444;
    color: #fff; font-size: 10px; display: flex; align-items: center; justify-content: center; gap: 10px; letter-spacing: .3px; }
  .slider-dots { left: 823px; top: 568px; display: flex; gap: 4px; }
  .slider-dots span { width: 17px; height: 16px; background: var(--red-soft); }
  .slider-dots span.active { background: var(--red); }

  .intro { left: 0; top: 638px; width: 1013px; text-align: center; }
  .intro h1 { font-size: 20px; font-weight: 500; color: var(--ink); letter-spacing: .3px; }
  .intro p { margin-top: 7px; font-family: "Inter", sans-serif; font-weight: 300; font-size: 18.5px; line-height: 24.5px; color: var(--ink-soft); }

  .divider { left: 104px; top: 749px; width: 805px; height: 1px; background: var(--line); }

  .section-title { left: 0; top: 785px; width: 1013px; text-align: center; font-size: 20px; font-weight: 500; letter-spacing: 1px; color: var(--ink); }

  .video { top: 844px; width: 241px; }
  .video-thumb { position: relative; width: 100%; height: 163px; }
  .play { position: absolute; left: 50%; top: 50%; width: 42px; height: 32px; margin: -16px 0 0 -21px; border-radius: 5px; background: rgba(20,20,20,.85); display: flex; align-items: center; justify-content: center; }
  .video-caption { margin-top: 10px; text-align: center; font-size: 9.5px; font-weight: 700; letter-spacing: .6px; color: #333; white-space: nowrap; }

  .social-band { left: 0; top: 1066px; width: 1013px; height: 59px; background: var(--band); border-top: 1px solid #e6e6e6; }
  .social-link { top: 1079px; width: 36px; height: 36px; border: 1.5px solid #333; display: flex; align-items: center; justify-content: center; }
  .social-link span { width: 6px; height: 6px; border-radius: 50%; background: #333; }
  .social-link.hover { background: var(--tweet-blue); border-color: var(--tweet-blue); }
  .social-link.hover span { background: #fff; }

  .site-footer { left: 0; top: 1125px; width: 1013px; height: 75px; background: var(--red); color: #fff; }
  .footer-nav a { position: absolute; top: 17px; color: #fff; text-decoration: none; font-size: 11px; font-weight: 700; letter-spacing: .3px; }
  .copyright { position: absolute; left: 102px; top: 44px; font-size: 10.5px; font-weight: 500; }
  .address { position: absolute; right: 101px; top: 42px; font-size: 10.5px; font-weight: 500; letter-spacing: .3px; }
</style>
</head>
<body>
  <div class="abs top-bar"></div>
  <div class="abs nav-marker"></div>

  <header>
    <div class="abs brand"><span class="brand-dot"></span><span class="brand-name">Iron Heron</span></div>
    <nav class="abs main-nav">
      <a class="current" href="#" style="left:598px">Home page</a>
      <a href="#" style="left:745px">Artists</a>
      <a href="#" style="left:853px">Contact</a>
    </nav>
  </header>

  <section class="hero">
    <div class="abs hero-photo" role="img" aria-label="Black and white portrait photograph of the featured artist with red lips"></div>
    <div class="abs hero-name">Marisol Vane</div>
    <div class="abs more-details">MORE DETAILS
      <svg width="14" height="6" viewBox="0 0 14 6"><path d="M0 3h12M9.5 .5L13 3 9.5 5.5" stroke="#fff" stroke-width="1" fill="none"/></svg>
    </div>
    <div class="abs slider-dots"><span class="active"></span><span></span><span></span><span></span><span></span><span></span></div>
  </section>

  <section class="abs intro">
    <h1>MUSIC FOR PICTURE. MUSIC FOR RADIO. MUSIC BY IRON HERON.</h1>
    <p>Iron Heron is one of the UK’s independent music production companies,<br>producing the highest quality Soul/Classic Brelvane music in London.</p>
  </section>

  <div class="abs divider"></div>

  <h2 class="abs section-title">RECENT VIDEOS</h2>

  <article class="abs video" style="left:100px">
    <div class="video-thumb" role="img" aria-label="Video still of a singer seated on a leather booth before a brick wall" style="background:linear-gradient(180deg,#5a4236 0%,#3a2a22 45%,#1c1410 100%)">
      <span class="play"><svg width="12" height="14" viewBox="0 0 12 14"><path d="M0 0L12 7 0 14z" fill="#fff"/></svg></span>
    </div>
    <div class="video-caption">DESMOND HARLOW &amp; THE KINFOLK BAND</div>
  </article>

  <article class="abs video" style="left:387px">
    <div class="video-thumb" role="img" aria-label="Video still of a singer in glasses framed by white flower garlands" style="background:radial-gradient(ellipse at 50% 45%,#b8664a 0%,#7a2a1e 45%,#2a0c0a 100%)">
      <span class="play"><svg width="12" height="14" viewBox="0 0 12 14"><path d="M0 0L12 7 0 14z" fill="#fff"/></svg></span>
    </div>
    <div class="video-caption">TOBIAS WRENFIELD - SHAKE IT LOOSE</div>
  </article>

  <article class="abs video" style="left:671px;width:239px">
    <div class="video-thumb" role="img" aria-label="Video still of a singer in soft purple light" style="background:linear-gradient(135deg,#2a1e2a 0%,#4a3038 45%,#1a1222 100%)">
      <span class="play"><svg width="12" height="14" viewBox="0 0 12 14"><path d="M0 0L12 7 0 14z" fill="#fff"/></svg></span>
    </div>
    <div class="video-caption">MARISOL VANE - QUIET STORM</div>
  </article>

  <div class="abs social-band"></div>
  <a class="abs social-link" href="#" aria-label="Social profile one" style="left:389px"><span></span></a>
  <a class="abs social-link hover" href="#" aria-label="Social profile two" style="left:457px"><span></span></a>
  <a class="abs social-link" href="#" aria-label="Social profile three" style="left:525px"><span></span></a>
  <a class="abs social-link" href="#" aria-label="Social profile four" style="left:587px"><span></span></a>

  <footer class="abs site-footer">
    <nav class="footer-nav">
      <a href="#" style="left:381px">Home page</a>
      <a href="#" style="left:504px">Artists</a>
      <a href="#" style="left:594px">Contact</a>
    </nav>
    <div class="copyright">Copyright © 2014 Iron Heron. All Rights Reserved.</div>
    <div class="address">27 Halden Row London, UK</div>
  </footer>
</body>
</html>
```